Book cover for LS

Design cover for a book of gratitude and inspiration.
Book trim size will be 6.5 x 6.5 inches, or 8 x 8 inches, hardcover, 96 pages
Title: Lantern Stones
Subtitle: A Book of Gratitude and Inspiration
Author: Carl Wendover

```html
<!DOCTYPE html>
<html lang="en">
<head>
<meta charset="utf-8">
<title>Lantern Stones — Book Cover</title>
<link rel="stylesheet" href="https://fonts.googleapis.com/css2?family=Playfair+Display:wght@400;700;800&family=Great+Vibes&family=Yellowtail&display=swap">
<style>
  :root {
    --stage: #5e5450;
    --title-blue: #2f5478;
    --title-blue-deep: #2a4660;
    --subtitle-grey: #4b4848;
    --frame-white: rgba(255, 255, 255, 0.85);
    --wash-cream: #fbf2e6;
    --wash-peach: #f3c9a0;
    --wash-orange: #e9a15f;
    --wash-rose: #eeb2a6;
    --wash-sky: #dcebea;
    --badge-text: #ffffff;
  }

  html, body {
    margin: 0;
    padding: 0;
    width: 1200px;
    height: 796px;
    overflow: hidden;
    background: var(--stage);
  }

  .stage {
    position: relative;
    width: 1200px;
    height: 796px;
    display: flex;
    align-items: center;
    justify-content: center;
  }

  .cover {
    position: relative;
    width: 720px;
    height: 720px;
    overflow: hidden;
  }

  .cover__artwork {
    position: absolute;
    inset: 0;
    background:
      radial-gradient(ellipse 45% 40% at 50% 55%, rgba(255, 252, 246, 0.95), rgba(255, 252, 246, 0) 70%),
      radial-gradient(ellipse 40% 30% at 55% 12%, var(--wash-sky), rgba(220, 235, 234, 0) 75%),
      radial-gradient(ellipse 30% 45% at 10% 40%, var(--wash-orange), rgba(233, 161, 95, 0) 75%),
      radial-gradient(ellipse 35% 35% at 12% 85%, var(--wash-rose), rgba(238, 178, 166, 0) 75%),
      radial-gradient(ellipse 35% 35% at 88% 85%, var(--wash-peach), rgba(243, 201, 160, 0) 75%),
      linear-gradient(135deg, #f6d9b8 0%, var(--wash-cream) 45%, #f7e3cf 100%);
  }

  .cover__frame {
    position: absolute;
    left: 42px;
    top: 42px;
    right: 42px;
    bottom: 42px;
    border: 5px solid var(--frame-white);
    box-shadow: 0 0 6px rgba(255, 255, 255, 0.6);
  }

  .cover__title {
    position: absolute;
    left: 0;
    right: 0;
    top: 112px;
    margin: 0;
    text-align: center;
    font-weight: normal;
  }

  .cover__title-caps {
    display: block;
    font-family: "Playfair Display", serif;
    font-weight: 800;
    font-size: 78px;
    line-height: 1;
    letter-spacing: 1px;
    color: var(--title-blue-deep);
  }

  .cover__title-script {
    display: block;
    margin-top: -14px;
    font-family: "Great Vibes", cursive;
    font-size: 150px;
    line-height: 1;
    color: var(--title-blue);
  }

  .cover__subtitle {
    position: absolute;
    left: 0;
    right: 0;
    top: 362px;
    margin: 0;
    text-align: center;
    color: var(--subtitle-grey);
  }

  .cover__subtitle-lead {
    display: block;
    font-family: "Playfair Display", serif;
    font-size: 42px;
    line-height: 1.1;
  }

  .cover__subtitle-script {
    display: block;
    font-family: "Yellowtail", cursive;
    font-size: 58px;
    line-height: 1.05;
  }

  .cover__subtitle-amp {
    font-family: "Playfair Display", serif;
    font-size: 34px;
  }

  .cover__byline {
    position: absolute;
    left: 0;
    right: 0;
    top: 562px;
    text-align: center;
  }

  .cover__byline-label {
    display: block;
    font-family: "Playfair Display", serif;
    font-size: 23px;
    letter-spacing: 0.5px;
    color: var(--subtitle-grey);
  }

  .cover__author {
    display: inline-block;
    margin-top: 6px;
    width: 168px;
    height: 38px;
    line-height: 40px;
    border-radius: 7px;
    background: var(--title-blue);
    font-family: "Yellowtail", cursive;
    font-size: 25px;
    color: var(--badge-text);
  }
</style>
</head>
<body>
  <main class="stage">
    <article class="cover">
      <div class="cover__artwork" role="img" aria-label="Soft watercolour wash of autumn leaves in orange, peach and rose framing the left side and lower right corner on a pale cream and sky-blue ground"></div>
      <div class="cover__frame"></div>

      <h1 class="cover__title">
        <span class="cover__title-caps">LANTERN</span>
        <span class="cover__title-script">Stones</span>
      </h1>

      <p class="cover__subtitle">
        <span class="cover__subtitle-lead">A Book of</span>
        <span class="cover__subtitle-script">Gratitude <span class="cover__subtitle-amp">&amp;</span> Inspiration</span>
      </p>

      <div class="cover__byline">
        <span class="cover__byline-label">Author</span>
        <span class="cover__author">Carl Wendover</span>
      </div>
    </article>
  </main>
</body>
</html>
```